BrivoPeak Business Card Design Project

We are looking for a modern, clean business card design for our new company. We are a consulting firm focused on the financial services market providing management and IT consulting to banks, insurance companies, etc. Please include our company logo and company contact information from the attached file in the design. Two versions of the logo are attached, either version is acceptable. Logos are available in other file formats if needed. We would like to include the contact information for both our UK and US offices as well as the following information for each individual card holder: Name, position/title, address, phone number and e-mail address.
Updates
Project Deadline Extended
Reason: A last minute trip over seas has prevented us from finalizing the decision. A decision will be made this week. We apologize for the inconvenience.
Industry/Entity Type
Business
Contact Information for Business Card
Company logo.
Company locations and phone numbers for both the US and UK offices.
Company URL.
Cardholder Name
Cardholder Position/title
Cardholder Address
Cardholder Phone Number
Cardholder e-mail Address
Look and feel
Each slider illustrates characteristics of the customer's brand and the style your logo design should communicate.

```html
<!DOCTYPE html>
<html lang="en">
<head>
<meta charset="utf-8">
<title>BrivoPeak Partners – Business Card</title>
<link rel="stylesheet" href="https://fonts.googleapis.com/css2?family=Open+Sans:wght@400;600;700&display=swap">
<style>
  :root {
    --navy: #1f3257;
    --navy-deep: #18284a;
    --grey: #8a8c90;
    --grey-light: #c9cacd;
    --white: #ffffff;
    --stage: #2b2c2e;
  }
  * { margin: 0; padding: 0; box-sizing: border-box; }
  html, body { width: 1200px; height: 802px; overflow: hidden; }
  body {
    background: var(--stage);
    font-family: "Open Sans", Arial, sans-serif;
    position: relative;
  }
  .card {
    position: absolute;
    top: 241px;
    width: 560px;
    height: 320px;
    overflow: hidden;
    box-shadow: 0 10px 30px rgba(0,0,0,.5);
  }
  .card--back {
    left: 27px;
    background: linear-gradient(160deg, #2a4170 0%, var(--navy) 55%, var(--navy-deep) 100%);
    color: var(--white);
    display: flex;
    flex-direction: column;
    align-items: center;
    justify-content: center;
  }
  .brand {
    font-weight: 700;
    line-height: 1;
    display: flex;
    align-items: center;
    gap: 12px;
  }
  .brand__square {
    width: 18px; height: 18px;
    background: currentColor;
  }
  .card--back .brand { font-size: 50px; }
  .card--back .brand__sub {
    font-size: 17px; font-weight: 700; letter-spacing: 4px; margin-top: 8px;
  }
  .card--back .url {
    margin-top: 18px; font-size: 14px; letter-spacing: 2.5px; font-weight: 600;
  }
  .card--front { left: 613px; background: var(--white); }
  .front__art { position: absolute; inset: 0; }
  .front__brand {
    position: absolute; left: 42px; top: 48px; color: var(--navy);
  }
  .front__brand .brand { font-size: 36px; }
  .front__brand .brand__sub {
    font-size: 14px; font-weight: 700; letter-spacing: 3px; color: var(--grey);
    margin: 6px 0 0 30px;
  }
  .holder { position: absolute; left: 42px; top: 148px; }
  .holder__name { font-size: 20px; font-weight: 600; color: var(--navy); }
  .holder__title { font-size: 12px; color: var(--grey); }
  .contact {
    position: absolute; list-style: none; color: var(--white); font-size: 12.5px; line-height: 1.45;
  }
  .contact li { display: flex; align-items: center; gap: 7px; }
  .contact svg { width: 12px; height: 12px; fill: var(--white); flex: none; }
  .contact--holder { left: 28px; bottom: 14px; }
  .contact--holder .indent { padding-left: 19px; }
  .contact--offices { right: 24px; top: 92px; text-align: right; font-size: 12px; }
  .contact--offices li { justify-content: flex-end; }
  .contact--offices .gap { margin-top: 14px; }
</style>
</head>
<body>

<section class="card card--back">
  <div class="brand"><span class="brand__square"></span>BrivoPeak</div>
  <div class="brand__sub">PARTNERS</div>
  <div class="url">www.brivopeakpartners.com</div>
</section>

<section class="card card--front">
  <svg class="front__art" viewBox="0 0 560 320" preserveAspectRatio="none" aria-hidden="true">
    <path d="M0,222 C130,222 215,205 282,135 C340,72 410,42 560,36 L560,320 L0,320 Z" fill="var(--navy)"/>
    <path d="M60,226 C170,224 235,190 290,125 C345,62 420,32 560,26 L560,36 C420,44 352,76 300,134 C240,200 170,228 60,226 Z" fill="var(--grey)"/>
    <path d="M0,215 C90,214 170,200 235,165 C185,200 110,212 0,208 Z" fill="var(--grey-light)"/>
  </svg>

  <div class="front__brand">
    <div class="brand"><span class="brand__square"></span>BrivoPeak</div>
    <div class="brand__sub">PARTNERS</div>
  </div>

  <div class="holder">
    <div class="holder__name">Daniel Brooke</div>
    <div class="holder__title">Founder</div>
  </div>

  <ul class="contact contact--holder">
    <li><svg viewBox="0 0 12 12"><path d="M1,3 C1,1.5 2,1 6,1 C10,1 11,1.5 11,3 L9,4 L8,3 L4,3 L3,4 Z M3,5 L9,5 L10,10 L2,10 Z"/></svg>0431 205 778</li>
    <li><svg viewBox="0 0 12 12"><path d="M1,2 H11 V10 H1 Z M1.8,2.8 L6,6.4 L10.2,2.8" fill="none" stroke="#fff" stroke-width="1.2"/></svg>cardholder@brivopeakmail.com</li>
    <li><svg viewBox="0 0 12 12"><path d="M6,1 L11.5,6 H10 V11 H7 V8 H5 V11 H2 V6 H0.5 Z"/></svg>99 demo street, demo place</li>
    <li class="indent">P.O. Box 000, 0000 Lacus, Avenue</li>
  </ul>

  <ul class="contact contact--offices">
    <li>UK: +44 7700 418 552 <svg viewBox="0 0 12 12"><path d="M1,3 C1,1.5 2,1 6,1 C10,1 11,1.5 11,3 L9,4 L8,3 L4,3 L3,4 Z M3,5 L9,5 L10,10 L2,10 Z"/></svg></li>
    <li>14 Harrow Court <svg viewBox="0 0 12 12"><path d="M6,1 L11.5,6 H10 V11 H7 V8 H5 V11 H2 V6 H0.5 Z"/></svg></li>
    <li>London, E2 4QP, Great Britain</li>
    <li class="gap">US: (555) 214-7730 <svg viewBox="0 0 12 12"><path d="M1,3 C1,1.5 2,1 6,1 C10,1 11,1.5 11,3 L9,4 L8,3 L4,3 L3,4 Z M3,5 L9,5 L10,10 L2,10 Z"/></svg></li>
    <li>718 N Cedar Ave, Suite 210 <svg viewBox="0 0 12 12"><path d="M6,1 L11.5,6 H10 V11 H7 V8 H5 V11 H2 V6 H0.5 Z"/></svg></li>
    <li>Millbrook CO 80512, United States</li>
  </ul>
</section>

</body>
</html>
```